Brightwell Assist Public Benefit Corporation - Initial Website

We need to develop an initial website for Brightwell Assist PBC. We are a startup managed business services provider focused on small business owners, entrepreneurs and their employees. We are a public benefit corporation and our public mission is to help business owners, entrepreneurs and their employees overcome the challenges that hold them back from reaching personal and professional success.
Our primary service offerings are managed business services that allow us to support the day-to-day operations of the businesses we support. This ongoing support provides the necessary pre-requisite relationship so we can provide effective and timely support when their organizations are experiencing challenges and moments of crisis. In those moments, it is our opportunity to help them overcome those challenges and stay on track for business utopia.
Our services are provided on a contract basis for a fixed monthly fee. We want to build strong relationships that help our clients grow their businesses while taking away the stresses associated with the backend of the business operations.
Finally, our public benefit is that we provide crisis invention, critical incident support, and mental health services to business owners and their employees during challenging times in an effort to improve their overall quality of life.

Coding

Coded - Design and coding required

```html
<!DOCTYPE html>
<html lang="en">
<head>
<meta charset="utf-8">
<title>Brightwell Assist Public Benefit Corporation</title>
<link rel="stylesheet" href="https://fonts.googleapis.com/css2?family=Hind:wght@600;700&family=Lato:wght@400;700;900&display=swap">
<style>
:root{
  --orange:#fb6a0a;
  --orange-deep:#f25a00;
  --navy:#0c1a4b;
  --peach:#fdeee3;
  --ink:#1d1d1d;
  --muted:#6b6b6b;
  --pale:#ffe3c9;
  --white:#ffffff;
}
*{box-sizing:border-box;margin:0;padding:0}
html,body{width:1200px;height:3195px;overflow:hidden;background:var(--white)}
body{position:relative;font-family:"Lato",sans-serif;color:var(--ink)}
.abs{position:absolute}
.heading{font-family:"Hind",sans-serif;font-weight:700;letter-spacing:1px;line-height:1}
.hl{color:var(--orange)}

/* header */
.brand{left:109px;top:24px}
.brand-name{font-family:"Lato",sans-serif;font-weight:400;font-size:44px;color:var(--orange);line-height:1;letter-spacing:.5px}
.brand-sub{font-family:"Hind",sans-serif;font-weight:700;font-size:23px;color:var(--navy);letter-spacing:.8px;margin-top:6px;line-height:1}
.btn-request{left:671px;top:22px;width:179px;height:42px;border-radius:21px;background:var(--navy);color:var(--white);font-weight:700;font-size:16px;display:flex;align-items:center;justify-content:center}
.call-icon{left:868px;top:23px;width:41px;height:41px;border-radius:50%;background:var(--orange)}
.call-label{left:925px;top:23px;font-size:12px;color:#333}
.call-number{left:925px;top:41px;font-size:22px;font-weight:900;color:var(--orange)}
.nav{top:88px;font-size:16px;color:#222}
.nav.active{color:var(--orange)}

/* hero */
.hero-title{left:0;width:1200px;top:220px;text-align:center;font-size:60px;color:var(--white)}
.hero-text{left:200px;width:800px;top:286px;text-align:center;color:var(--white);font-size:20px;line-height:34px}
.btn-pill{display:flex;align-items:center;border-radius:24px;font-weight:700}
.btn-pill .dot{width:34px;height:34px;border-radius:50%;margin:0 10px 0 4px;flex:none}
.btn-start{left:523px;top:367px;width:153px;height:42px;background:var(--navy);color:var(--white);font-size:16px}
.btn-start .dot{background:var(--orange)}
.btn-more{background:var(--orange);color:var(--white);font-size:16px;width:146px;height:42px}
.btn-more .dot{background:var(--navy)}

/* who */
.who-title{left:689px;top:920px;font-size:44px;color:var(--navy)}
.copy{font-size:15px;line-height:29px;color:var(--muted)}
.who-p1{left:689px;top:980px;width:400px}
.who-p2{left:689px;top:1112px;width:400px}

/* services */
.services{left:0;top:1453px;width:1200px;height:828px;background:linear-gradient(135deg,#f75d00 0%,#ff7a1a 45%,#f35c00 100%)}
.svc-title{left:0;width:1200px;top:1535px;text-align:center;font-size:46px;color:var(--white)}
.svc-sub{left:0;width:1200px;top:1588px;text-align:center;font-size:21px;font-weight:900;color:var(--pale)}
.card{width:310px;height:411px;top:1649px;background:var(--white);border-radius:25px}
.card-img{position:absolute;left:11px;top:12px;width:288px;height:251px;border-radius:20px}
.card-title{position:absolute;left:0;width:100%;top:286px;text-align:center;font-weight:900;font-size:16px;color:var(--navy)}
.card-text{position:absolute;left:25px;width:260px;top:310px;text-align:center;font-size:14px;line-height:25px;color:var(--muted)}

/* benefits */
.ben-title{left:120px;top:2343px;font-size:46px;color:var(--navy)}
.ben-p{left:120px;top:2398px;width:430px}
.bullets{left:145px;top:2530px;list-style:none;font-size:15px;color:#555}
.bullets li{height:29px;line-height:29px;display:flex;align-items:center}
.bullets svg{margin-right:12px}
.ben-img{left:609px;top:2291px;width:482px;height:449px;border-radius:80px;background:linear-gradient(160deg,#3b4a4c 0%,#6f8285 35%,#2e3a3c 70%,#1f2a2c 100%);box-shadow:0 10px 30px rgba(0,0,0,.15)}

/* footer */
.foot-brand{left:0;width:1200px;top:2945px;text-align:center}
.foot-brand .brand-name{color:var(--white);font-size:52px}
.foot-brand .brand-sub{color:var(--white);font-size:27px;margin-top:6px}
.foot-nav{top:3049px;font-size:19px;color:var(--white);transform:translateX(-50%)}
.foot-sep{top:3049px;font-size:19px;color:var(--white)}
.social{top:3096px;width:34px;height:34px;border-radius:50%;background:var(--orange)}
.copyright{left:0;width:1200px;top:3146px;text-align:center;font-size:13px;color:var(--white)}
</style>
</head>
<body>

<!-- header -->
<div class="abs brand">
  <div class="brand-name">Brightwell Assist</div>
  <div class="brand-sub">PUBLIC BENEFIT CORPORATION</div>
</div>
<div class="abs btn-request">Request A Service</div>
<div class="abs call-icon">
  <svg width="41" height="41" viewBox="0 0 41 41"><path d="M15 12c1-1 2-1 3 0l2 3c.6 1 .4 2-.4 2.6l-1.3 1c.8 2 2.2 3.5 4.2 4.4l1-1.3c.6-.8 1.7-1 2.6-.4l3 2c1 .7 1 2 0 3l-1.3 1.3c-1.2 1.2-3 1.5-4.6.8-4.5-2-7.8-5.3-9.8-9.8-.7-1.6-.4-3.4.8-4.6z" fill="#fff"/></svg>
</div>
<div class="abs call-label">Call Us</div>
<div class="abs call-number">+1 555 014 2030</div>
<div class="abs nav active" style="left:547px">Home</div>
<div class="abs nav" style="left:640px">About Us</div>
<div class="abs nav" style="left:757px">Our Services</div>
<div class="abs nav" style="left:900px">Benefits</div>
<div class="abs nav" style="left:1009px">Contact Us</div>

<!-- hero -->
<svg class="abs" style="left:0;top:0" width="1200" height="780" viewBox="0 0 1200 780">
  <defs>
    <linearGradient id="heroPhoto" x1="0" y1="0" x2="1" y2="1">
      <stop offset="0" stop-color="#2b2420"/>
      <stop offset=".45" stop-color="#4a3f38"/>
      <stop offset=".75" stop-color="#3a3532"/>
      <stop offset="1" stop-color="#1e1c1c"/>
    </linearGradient>
  </defs>
  <path d="M0 133H1200V595Q600 855 0 595Z" fill="url(#heroPhoto)" role="img" aria-label="Photo of a business team meeting around a laptop"/>
  <path d="M0 133H1200V595Q600 855 0 595Z" fill="rgba(10,10,20,.25)"/>
  <path d="M45 614Q600 907 1155 614Q600 848 45 614Z" fill="var(--orange)"/>
</svg>
<div class="abs heading hero-title">PUBLIC <span class="hl">BENEFIT</span> CORPORATION</div>
<div class="abs hero-text">Our public mission is to help business owners, entrepreneurs and their employees overcome the challenges</div>
<div class="abs btn-pill btn-start"><span class="dot"></span>Get Started</div>

<!-- who we are -->
<svg class="abs" style="left:0;top:800px" width="620" height="560" viewBox="0 800 620 560">
  <circle cx="124" cy="853" r="36" fill="var(--peach)"/>
  <circle cx="353" cy="1094" r="245" fill="var(--navy)"/>
  <circle cx="374" cy="1069" r="219" fill="var(--white)"/>
  <defs>
    <radialGradient id="whoPhoto" cx=".5" cy=".5" r=".6">
      <stop offset="0" stop-color="#4fa6ff"/>
      <stop offset=".5" stop-color="#1c3d72"/>
      <stop offset="1" stop-color="#0d1a33"/>
    </radialGradient>
  </defs>
  <circle cx="374" cy="1069" r="210" fill="url(#whoPhoto)" role="img" aria-label="Image of a hand holding a glowing network of people over a world map"/>
</svg>
<div class="abs heading who-title">WHO <span class="hl">WE ARE</span></div>
<p class="abs copy who-p1">We are a public benefit corporation and our public mission is to help business owners, entrepreneurs and their employees overcome the challenges that hold them back from reaching personal and professional success.</p>
<p class="abs copy who-p2">Sed ut perspiciatis unde omnis iste natus error sit voluptatem accusantium doloremque laudantium, totam rem aperiam, eaque ipsa quae ab illo</p>
<div class="abs btn-pill btn-more" style="left:689px;top:1224px"><span class="dot"></span>Read More</div>

<!-- services -->
<div class="abs services"></div>
<svg class="abs" style="left:0;top:2100px" width="1200" height="190" viewBox="0 2100 1200 190">
  <path d="M0 2281Q600 1985 1200 2281V2290H0Z" fill="var(--white)"/>
  <path d="M100 2240Q600 2010 1100 2240Q600 2035 100 2240Z" fill="var(--navy)"/>
</svg>
<div class="abs heading svc-title">SERVICES WE PROVIDE</div>
<div class="abs svc-sub">OUR SERVICES ARE PROVIDED ON A CONTRACT BASIS FOR A FIXED MONTHLY FEE</div>

<div class="abs card" style="left:113px">
  <div class="card-img" role="img" aria-label="Photo of a businesswoman touching a digital shield icon" style="background:linear-gradient(135deg,#3a3d48,#8a4f55 55%,#2d2f38)"></div>
  <div class="card-title">CRISIS INVENTION</div>
  <div class="card-text">Et quasi architecto beatae vitae dicta sunt explicabo. Nemo enim ipsam volup tatem quia voluptas sit asper</div>
</div>
<div class="abs card" style="left:445px">
  <div class="card-img" role="img" aria-label="Photo of two women checking a car beside the road" style="background:linear-gradient(135deg,#1f2a4a,#6b6a66 50%,#a29d86)"></div>
  <div class="card-title">CRITICAL INCIDENT SUPPORT</div>
  <div class="card-text">Et quasi architecto beatae vitae dicta sunt explicabo. Nemo enim ipsam volup tatem quia voluptas sit asper</div>
</div>
<div class="abs card" style="left:777px">
  <div class="card-img" role="img" aria-label="Photo of a woman leaping joyfully over a field" style="background:linear-gradient(180deg,#9db5b3,#c5cfc8 50%,#4a4a3c 80%,#3a3a30)"></div>
  <div class="card-title">MENTAL HEALTH SERVICES</div>
  <div class="card-text">Et quasi architecto beatae vitae dicta sunt explicabo. Nemo enim ipsam volup tatem quia voluptas sit asper</div>
</div>

<!-- benefits -->
<svg class="abs" style="left:0;top:2290px" width="60" height="120" viewBox="0 2290 60 120">
  <circle cx="0" cy="2347" r="44" fill="var(--peach)"/>
</svg>
<div class="abs heading ben-title">OUR <span class="hl">PUBLIC BENEFITS</span></div>
<p class="abs copy ben-p">We provide crisis invention, critical incident support, and mental health services to business owners and their employees during challenging times in an effort to improve their overall quality of life</p>
<ul class="abs bullets">
  <li><svg width="11" height="10" viewBox="0 0 11 10"><path d="M1 1l4 4-4 4M6 1l4 4-4 4" stroke="var(--orange)" stroke-width="1.5" fill="none"/></svg>Sed ut perspiciatis unde</li>
  <li><svg width="11" height="10" viewBox="0 0 11 10"><path d="M1 1l4 4-4 4M6 1l4 4-4 4" stroke="var(--orange)" stroke-width="1.5" fill="none"/></svg>Natus error sit voluptatem accusantium</li>
  <li><svg width="11" height="10" viewBox="0 0 11 10"><path d="M1 1l4 4-4 4M6 1l4 4-4 4" stroke="var(--orange)" stroke-width="1.5" fill="none"/></svg>Doloremque laudantium, totam rem aperiam</li>
</ul>
<div class="abs btn-pill btn-more" style="left:120px;top:2642px"><span class="dot"></span>Read More</div>
<div class="abs ben-img" role="img" aria-label="Photo of a team meeting in a glass-walled conference room"></div>

<!-- footer -->
<svg class="abs" style="left:0;top:2700px" width="1200" height="495" viewBox="0 2700 1200 495">
  <path d="M0 2733Q600 2971 1200 2733V3195H0Z" fill="var(--navy)"/>
  <path d="M99 2773Q600 2975 1101 2773Q600 2935 99 2773Z" fill="var(--orange)"/>
  <circle cx="615" cy="2784" r="42" fill="var(--peach)"/>
</svg>
<div class="abs foot-brand">
  <div class="brand-name">Brightwell Assist</div>
  <div class="brand-sub">PUBLIC BENEFIT CORPORATION</div>
</div>
<div class="abs foot-nav" style="left:262px">Home</div>
<div class="abs foot-sep" style="left:331px">|</div>
<div class="abs foot-nav" style="left:419px">About Us</div>
<div class="abs foot-sep" style="left:500px">|</div>
<div class="abs foot-nav" style="left:584px">Services</div>
<div class="abs foot-sep" style="left:662px">|</div>
<div class="abs foot-nav" style="left:745px">Benefits</div>
<div class="abs foot-sep" style="left:822px">|</div>
<div class="abs foot-nav" style="left:917px">Contact Us</div>
<div class="abs social" style="left:538px" role="img" aria-label="Social link"></div>
<div class="abs social" style="left:583px" role="img" aria-label="Social link"></div>
<div class="abs social" style="left:626px" role="img" aria-label="Social link"></div>
<div class="abs copyright">(C) Copyright 2024 | All Rights Reserved</div>

</body>
</html>
```